Window and GutterCleaning Flyer A5 size double sided.

We need a double sided A5 flyer. Side 1, is for window cleaning, side 2 is for gutter cleaning. Licensed by Borough of Halvern Council.
Phone number 0800 315 4720.
Business address 7 Tarnlow Brae, North Pellin Edinburgh EH14 3RW.
www.clearpane-vista-services.com
We use a LoftPro Gutter inspection Cam to view your gutters first to see if they need doing.
Window cleaning ; Professional window cleaning services, what we offer, water fed pole window cleaning able to reach windows up to 60 feet.
Conservatory cleaning.
Conservatory roof cleaning.
Fascias & Soffits cleaning.
Excellent Customer Service.
Target Market(s)
domestic houses
Industry/Entity Type
window cleaning
Look and feel
Each slider illustrates characteristics of the customer's brand and the style your logo design should communicate.

```html
<!DOCTYPE html>
<html lang="en">
<head>
<meta charset="utf-8">
<title>Clearpane Vista – Window and Gutter Cleaning Flyer</title>
<link rel="stylesheet" href="https://fonts.googleapis.com/css2?family=Montserrat:wght@500;700&family=Roboto:wght@400;700&family=Roboto+Condensed:wght@400&display=swap">
<style>
:root{
  --sky:#9fc9ec;
  --navy:#2f2c6e;
  --ink:#1b1b1b;
  --paper:#ffffff;
  --stage:#ecebe8;
  --arrow-green:#3e8a3a;
}
*{margin:0;padding:0;box-sizing:border-box}
html,body{width:1200px;height:928px;overflow:hidden;background:var(--stage)}
body{position:relative;font-family:"Roboto",Arial,sans-serif;color:var(--ink)}
.flyer{position:absolute;top:82px;width:538px;height:764px;background:var(--paper);overflow:hidden;box-shadow:0 2px 8px rgba(0,0,0,.12)}
.flyer--windows{left:44px}
.flyer--gutters{left:617px}
.abs{position:absolute}
.header{left:0;top:0;width:100%;height:126px;background:var(--sky)}
.wave{position:absolute;left:0;width:100%;display:block}
.brand{left:22px;top:52px;display:flex;align-items:center;gap:8px;font-family:"Montserrat",Arial,sans-serif;font-weight:700;font-size:20px;color:var(--navy)}
.brand-mark{width:13px;height:13px;background:var(--navy)}
.contact-label{right:28px;top:40px;font-family:"Montserrat",Arial,sans-serif;font-weight:500;font-size:15px;color:var(--navy)}
.contact-phone{right:20px;top:62px;display:flex;align-items:center;gap:10px;font-family:"Roboto Condensed",Arial,sans-serif;font-size:36px;line-height:40px;color:var(--navy);white-space:nowrap}
.title{left:20px;top:148px;font-size:19.5px;font-weight:400}
.lead{left:20px;top:182px;width:490px;font-size:14.5px;line-height:22.6px}
.photo{position:absolute}
.body-copy{left:12px;top:568px;width:520px;font-size:14.5px;line-height:22.6px}
.footer-line{left:17px;display:flex;align-items:center;gap:8px;font-size:12.5px;line-height:18px;color:var(--sky);white-space:nowrap}
.license-box{left:370px;top:696px;width:152px;height:57px;background:var(--sky);color:var(--navy);font-family:"Roboto Condensed",Arial,sans-serif;font-size:14px;line-height:18px;text-align:center;padding-top:10px;white-space:nowrap;letter-spacing:-.1px}
.intro{left:0;top:148px;width:100%;text-align:center;font-size:14.5px;line-height:22.6px}
.service-band{left:0;top:280px;width:100%;height:112px;background:var(--sky)}
.service-label{top:341px;width:170px;text-align:center;font-size:15px;line-height:19px;color:var(--navy)}
.arrow-tag{position:absolute;height:22px;background:var(--arrow-green);color:#fff;font:700 11.5px/22px "Roboto",Arial,sans-serif;padding:0 18px 0 8px;clip-path:polygon(0 0,82% 0,100% 50%,82% 100%,0 100%)}
.cam-copy{left:25px;top:464px;width:200px;font-size:14.5px;line-height:22.6px}
.service-note{left:178px;top:698px;font-family:"Roboto Condensed",Arial,sans-serif;font-size:17.5px;line-height:22px;color:var(--sky)}
.experience-box{left:358px;top:684px;width:150px;height:57px;background:var(--sky);color:var(--navy);font-family:"Roboto Condensed",Arial,sans-serif;font-size:15.5px;line-height:20px;text-align:center;padding-top:8px;white-space:nowrap}
</style>
</head>
<body>

<section class="flyer flyer--windows" aria-label="Side one: window cleaning">
  <div class="abs header"></div>
  <svg class="wave" style="top:112px" width="538" height="24" viewBox="0 0 538 24" preserveAspectRatio="none" aria-hidden="true">
    <path d="M0 12 C110 4 210 16 310 8 C400 2 470 6 538 10 L538 24 L0 24 Z" fill="var(--paper)"/>
  </svg>
  <div class="abs brand"><span class="brand-mark"></span>Clearpane Vista</div>
  <div class="abs contact-label">For More Information Contact Us</div>
  <div class="abs contact-phone">
    <svg width="34" height="34" viewBox="0 0 38 38" aria-hidden="true"><circle cx="19" cy="19" r="17" fill="none" stroke="var(--navy)" stroke-width="2.4"/><path d="M13 11c2-1 3 0 4 3s-1 3-1 4 2 4 3 5 2-1 4 0 3 3 1 4c-5 2-13-7-11-16z" fill="var(--navy)"/></svg>
    0800 315 4720
  </div>

  <h1 class="abs title">Professional Window Cleaning Services.</h1>
  <p class="abs lead">What We Offer, Water Fed Pole, Window Cleaning Able To Reach<br>Windows Up To 60 Feet.</p>

  <div class="photo" role="img" aria-label="Water fed pole brush scrubbing a wet window" style="left:0;top:239px;width:161px;height:323px;background:linear-gradient(160deg,#a9c6e6,#6f92c1 60%,#3e5f97)"></div>
  <div class="photo" role="img" aria-label="Brick house with a cleaning pole reaching upper windows" style="left:166px;top:239px;width:131px;height:323px;background:linear-gradient(180deg,#b9b3a6,#9a5a45 40%,#84503e 80%,#c7b07a)"></div>
  <div class="photo" role="img" aria-label="Close view of pole brush cleaning a white framed window" style="left:304px;top:239px;width:234px;height:323px;background:linear-gradient(135deg,#e8ecef,#9aa7b2 50%,#4f5b65)"></div>

  <p class="abs body-copy">Regular window cleaning helps to avoid the build-up of dirt and residue on the glass, meaning more light can get into your home or premises.</p>

  <svg class="wave" style="top:630px" width="538" height="134" viewBox="0 0 538 134" preserveAspectRatio="none" aria-hidden="true">
    <path d="M0 14 C110 4 220 4 330 16 C420 26 490 26 538 22 L538 134 L0 134 Z" fill="var(--navy)"/>
  </svg>
  <div class="abs footer-line" style="top:671px">
    <svg width="19" height="15" viewBox="0 0 20 16" aria-hidden="true"><rect x="1" y="2" width="18" height="12" fill="none" stroke="var(--sky)" stroke-width="1.6"/><path d="M1 2l9 7 9-7" fill="none" stroke="var(--sky)" stroke-width="1.6"/></svg>
    info@clearpane-vista-services.com
  </div>
  <div class="abs footer-line" style="top:701px">
    <svg width="19" height="19" viewBox="0 0 20 20" aria-hidden="true"><circle cx="10" cy="10" r="8.5" fill="none" stroke="var(--sky)" stroke-width="1.5"/><ellipse cx="10" cy="10" rx="4" ry="8.5" fill="none" stroke="var(--sky)" stroke-width="1.3"/><path d="M2 10h16M3.5 6h13M3.5 14h13" stroke="var(--sky)" stroke-width="1.2"/></svg>
    www.clearpane-vista-services.com
  </div>
  <div class="abs footer-line" style="top:731px">
    <svg width="19" height="21" viewBox="0 0 20 22" aria-hidden="true"><path d="M10 1a7 7 0 0 0-7 7c0 5 7 13 7 13s7-8 7-13a7 7 0 0 0-7-7z" fill="var(--sky)"/><circle cx="10" cy="8" r="2.6" fill="var(--navy)"/></svg>
    7 Tarnlow Brae, North Pellin, Edinburgh EH14 3RW
  </div>
  <div class="abs license-box">Licensed by<br>Borough of Halvern Council</div>
</section>

<section class="flyer flyer--gutters" aria-label="Side two: gutter cleaning">
  <div class="abs header"></div>
  <svg class="wave" style="top:112px" width="538" height="24" viewBox="0 0 538 24" preserveAspectRatio="none" aria-hidden="true">
    <path d="M0 12 C110 4 210 16 310 8 C400 2 470 6 538 10 L538 24 L0 24 Z" fill="var(--paper)"/>
  </svg>
  <div class="abs brand"><span class="brand-mark"></span>Clearpane Vista</div>
  <div class="abs contact-label">For More Information Contact Us</div>
  <div class="abs contact-phone">
    <svg width="34" height="34" viewBox="0 0 38 38" aria-hidden="true"><circle cx="19" cy="19" r="17" fill="none" stroke="var(--navy)" stroke-width="2.4"/><path d="M13 11c2-1 3 0 4 3s-1 3-1 4 2 4 3 5 2-1 4 0 3 3 1 4c-5 2-13-7-11-16z" fill="var(--navy)"/></svg>
    0800 315 4720
  </div>

  <p class="abs intro">Gutters are an important part of your home. So why not set up an annual plan<br>&amp; make sure you don’t run into problems when winter comes.</p>

  <div class="abs service-band"></div>
  <svg class="wave" style="top:390px" width="538" height="20" viewBox="0 0 538 20" preserveAspectRatio="none" aria-hidden="true">
    <path d="M0 0 L538 0 L538 4 C440 0 350 0 260 6 C170 12 80 12 0 8 Z" fill="var(--sky)"/>
  </svg>
  <div class="photo" role="img" aria-label="Conservatory with glass roof on a brick house" style="left:0;top:206px;width:170px;height:131px;background:linear-gradient(180deg,#9cc4e2,#dfe6ec 45%,#a8563f 75%,#7b3f2e)"></div>
  <div class="photo" role="img" aria-label="Mossy conservatory roof panels being cleaned" style="left:185px;top:206px;width:170px;height:131px;background:linear-gradient(160deg,#c7b9a5,#7c8060 40%,#a9b2b9 70%,#dfe3e7)"></div>
  <div class="photo" role="img" aria-label="Roofline of a house showing gutter, fascia and soffit" style="left:368px;top:206px;width:170px;height:131px;background:linear-gradient(200deg,#f4f4f4,#d9dadc 50%,#a86652)"></div>
  <div class="arrow-tag" style="left:400px;top:218px">Gutter</div>
  <div class="arrow-tag" style="left:378px;top:255px">Fascia</div>
  <div class="arrow-tag" style="left:368px;top:296px">Soffit</div>
  <div class="abs service-label" style="left:0">Conservatory<br>Cleaning</div>
  <div class="abs service-label" style="left:185px">Conservatory<br>Roof Cleaning</div>
  <div class="abs service-label" style="left:368px">Fascias And<br>Soffits Cleaning</div>

  <p class="abs cam-copy">We Use A LoftPro Gutter Inspection Cam To View Your Gutters First To See If They Need Doing.</p>
  <div class="photo" role="img" aria-label="Handheld inspection camera screen above a gutter being checked" style="left:222px;top:421px;width:150px;height:182px;background:linear-gradient(170deg,#4b4f55,#8d98a3 45%,#d3d6d1 70%,#8a8f7e)"></div>
  <div class="photo" role="img" aria-label="Vacuum pole clearing leaves from a roof gutter" style="left:372px;top:428px;width:142px;height:175px;background:linear-gradient(200deg,#8aa06a,#6f8f4e 45%,#9da1a6 75%,#5e5f63)"></div>

  <svg class="wave" style="top:618px" width="538" height="146" viewBox="0 0 538 146" preserveAspectRatio="none" aria-hidden="true">
    <path d="M0 12 C130 2 240 4 350 18 C440 28 500 28 538 24 L538 146 L0 146 Z" fill="var(--navy)"/>
  </svg>
  <div class="photo" role="img" aria-label="Smiling customer service agent wearing a headset" style="left:17px;top:599px;width:139px;height:165px;background:radial-gradient(ellipse at 55% 40%,#e6c7a8,#c89a6a 45%,#d9d2c8 75%,var(--navy) 100%)"></div>
  <div class="abs service-note">Excellent<br>Customer Service.</div>
  <div class="abs experience-box">With Over<br>30 Years Experience</div>
</section>

</body>
</html>
```